Online-Marketing Material für Recruiting-Plattform
Zielgruppe
Recruiting-Plattform für Physiotherapeuten. Wir sind Vermittler.
Aufgabenstellung
Ich benötige ein 2er Set aus Social-Media-Templates, das wir als Basis für Recruiting-Ads nutzen können.
Variante 1: (1080 x 1350) mit jeweils 285 Pixel Safe Space oben und unten (hier keine wichtigen Elemente).
Wichtig: Es handelt sich um ein Template. Daher muss es mit verschiedenen Elementen und Fotos funktionieren.
Die Elemente werden später durch variable Inhalte gesetzt. Ziel ist es, ein möglichst flexibles Format zu schaffen,
das mit unterschiedlichen Inhalten funktioniert.
Bitte orientiere dich am Grunddesign der Website therapunkt.de
Elemente und zugehörige Beispiele sind
1. Foto in querformat | Beispiel als Download)
2. Jobtitel als Headline | (Physiotherapeut (m/w/d)
3. Subtitle | Werde Teil eines wachsenden Teams
4. Arbeitszeitmodell | Vollzeit, Teilzeit
3. Ort | Hannover
4. 3 x Highlights | 1. Betriebliche Krankenversicherung 2. Tretlux 3. Gehalt bis zu 4.500 EUR
(Die Highlight variieren thematisch, daher hier bitte nur mit thematisch-neutralen Icons arbeiten.
5. Logo des Arbeitgebers (lusen) auf weiß
Variante 2 mit Foto in hochformat

```html
<!DOCTYPE html>
<html lang="de">
<head>
<meta charset="utf-8">
<title>lusen – Recruiting Templates</title>
<link href="https://fonts.googleapis.com/css2?family=Mulish:wght@500;800&family=Raleway:ital,wght@1,700;1,800&family=Roboto:wght@500&display=swap" rel="stylesheet">
<style>
  :root{
    --stage:#033a48;
    --teal:#00929a;
    --teal-soft:#35aaae;
    --yellow:#fbc23a;
    --ink:#0c3a46;
    --paper:#ffffff;
    --mist:#f3f3f3;
    --pin:#c8222c;
  }
  *{margin:0;padding:0;box-sizing:border-box}
  html,body{width:1200px;height:1048px;overflow:hidden;background:var(--stage)}
  .stage{position:relative;width:1200px;height:1048px}
  .card{position:absolute;top:200px;width:518px;height:648px;background:var(--paper);overflow:hidden}
  .card--landscape{left:60px}
  .card--portrait{left:622px}
  .shapes{position:absolute;inset:0}
  .abs{position:absolute;white-space:nowrap}
  .headline{font-family:"Mulish",sans-serif;color:var(--ink);font-size:28px;line-height:31px;letter-spacing:.2px}
  .headline .light{font-weight:500;display:block}
  .headline .bold{font-weight:800;display:block}
  .job-title{font-family:"Raleway",sans-serif;font-style:italic;font-weight:800;color:var(--paper);font-size:21px;transform:rotate(-2deg);transform-origin:left bottom}
  .job-title small{font-size:13px;font-weight:700}
  .work-model{font-family:"Raleway",sans-serif;font-style:italic;font-weight:800;color:var(--paper);font-size:16px;transform:rotate(-2deg);transform-origin:left bottom}
  .highlight{font-family:"Roboto",sans-serif;font-weight:500;color:var(--ink);font-size:16.5px;line-height:21px}
  .location{font-family:"Roboto",sans-serif;font-weight:500;color:var(--ink);font-size:13px}
  .brand{font-family:"Mulish",sans-serif;font-weight:500;color:var(--paper);display:flex;align-items:center;gap:8px}
  .brand .dot{display:inline-block;border-radius:50%;background:var(--paper)}
  .icon{position:absolute;width:16px;height:16px}
</style>
</head>
<body>
<main class="stage">

  <!-- Variante 1: Foto im Querformat -->
  <section class="card card--landscape">
    <svg class="shapes" viewBox="0 0 518 648" width="518" height="648">
      <polygon points="323,0 518,0 518,325 343,328" fill="var(--teal)"/>
      <polygon points="0,461 518,429 518,648 0,648" fill="var(--mist)"/>
      <polygon points="0,240 322,229 322,264 0,276" fill="var(--yellow)"/>
      <polygon points="0,277 169,270 169,301 0,306" fill="var(--teal-soft)"/>
      <g transform="rotate(-2 363 384)">
        <rect x="228" y="292" width="276" height="198" fill="#000" opacity=".12" transform="translate(3,4)"/>
        <rect x="226" y="286" width="276" height="198" fill="var(--paper)"/>
        <rect x="234" y="292" width="260" height="182" fill="url(#photoLandscape)" role="img" aria-label="Foto: Physiotherapeutin behandelt einen Patienten auf der Liege"/>
      </g>
      <defs>
        <linearGradient id="photoLandscape" x1="0" y1="0" x2="1" y2="1">
          <stop offset="0" stop-color="#c9d6d8"/>
          <stop offset=".55" stop-color="#e9eded"/>
          <stop offset="1" stop-color="#8d9aa3"/>
        </linearGradient>
      </defs>
    </svg>

    <div class="abs brand" style="left:367px;top:180px;font-size:32px">lusen<span class="dot" style="width:18px;height:18px"></span></div>

    <h1 class="abs headline" style="left:33px;top:157px"><span class="light">Werde Teil eines</span><span class="bold">wachsenden Teams</span></h1>
    <div class="abs job-title" style="left:36px;top:233px">Physiotherapeut (m/w/d)</div>
    <div class="abs work-model" style="left:34px;top:276px">Vollzeit, Teilzeit</div>

    <svg class="icon" style="left:32px;top:326px" viewBox="0 0 16 16"><path d="M8 14 2 8a3.4 3.4 0 0 1 6-4 3.4 3.4 0 0 1 6 4z" fill="var(--yellow)"/></svg>
    <div class="abs highlight" style="left:53px;top:322px">Betriebliche<br>Krankenversicherung</div>
    <svg class="icon" style="left:32px;top:372px" viewBox="0 0 16 16"><rect x="1" y="4" width="14" height="10" rx="1.5" fill="var(--yellow)"/><rect x="5.5" y="2" width="5" height="3" rx="1" fill="none" stroke="var(--yellow)" stroke-width="1.4"/><rect x="1" y="8" width="14" height="1" fill="var(--paper)"/></svg>
    <div class="abs highlight" style="left:53px;top:369px">Tretlux</div>
    <svg class="icon" style="left:32px;top:399px;height:19px" viewBox="0 0 16 19"><path d="M5 1h6l-2 4H7z" fill="var(--yellow)"/><path d="M6 5h4c4 3 5 7 4 10-1 3-11 3-12 0-1-3 0-7 4-10z" fill="var(--yellow)"/></svg>
    <div class="abs highlight" style="left:53px;top:398px">Gehalt bis zu<br>4.500 EUR</div>

    <svg class="icon" style="left:34px;top:478px;width:13px" viewBox="0 0 13 16"><path d="M6.5 16S1 10 1 6.2a5.5 5.5 0 0 1 11 0C12 10 6.5 16 6.5 16z" fill="var(--pin)"/><circle cx="6.5" cy="6.2" r="2.3" fill="var(--paper)"/></svg>
    <div class="abs location" style="left:53px;top:478px">Ort: Hannover</div>
  </section>

  <!-- Variante 2: Foto im Hochformat -->
  <section class="card card--portrait">
    <svg class="shapes" viewBox="0 0 518 648" width="518" height="648">
      <polygon points="0,480 518,449 518,648 0,648" fill="var(--mist)"/>
      <polygon points="0,0 114,0 141,648 0,648" fill="var(--teal)"/>
      <polygon points="233,251 518,240 518,276 233,287" fill="var(--yellow)"/>
      <polygon points="235,289 397,282 397,313 235,319" fill="var(--teal-soft)"/>
      <polygon points="2,170 231,162 245,494 2,502" fill="#000" opacity=".12"/>
      <polygon points="0,166 229,158 242,489 0,497" fill="var(--paper)"/>
      <polygon points="0,174 221,166 234,481 0,489" fill="url(#photoPortrait)" role="img" aria-label="Foto: heller Behandlungsraum mit Therapieliege und Fenster"/>
      <polygon points="0,178 121,176 123,230 0,234" fill="var(--teal)" opacity=".9"/>
      <defs>
        <linearGradient id="photoPortrait" x1="0" y1="0" x2="0" y2="1">
          <stop offset="0" stop-color="#efe7d6"/>
          <stop offset=".55" stop-color="#e6dcc8"/>
          <stop offset="1" stop-color="#54575b"/>
        </linearGradient>
      </defs>
    </svg>

    <div class="abs brand" style="left:16px;top:190px;font-size:19px;gap:5px">lusen<span class="dot" style="width:11px;height:11px"></span></div>

    <h1 class="abs headline" style="left:245px;top:174px"><span class="light">Werde Teil eines</span><span class="bold">wachsenden Teams</span></h1>
    <div class="abs job-title" style="left:261px;top:245px">Physiotherapeut <small>(m/w/d)</small></div>
    <div class="abs work-model" style="left:259px;top:288px">Vollzeit, Teilzeit</div>

    <svg class="icon" style="left:266px;top:334px" viewBox="0 0 16 16"><path d="M8 14 2 8a3.4 3.4 0 0 1 6-4 3.4 3.4 0 0 1 6 4z" fill="var(--yellow)"/></svg>
    <div class="abs highlight" style="left:287px;top:330px">Betriebliche<br>Krankenversicherung</div>
    <svg class="icon" style="left:266px;top:380px" viewBox="0 0 16 16"><rect x="1" y="4" width="14" height="10" rx="1.5" fill="var(--yellow)"/><rect x="5.5" y="2" width="5" height="3" rx="1" fill="none" stroke="var(--yellow)" stroke-width="1.4"/><rect x="1" y="8" width="14" height="1" fill="var(--paper)"/></svg>
    <div class="abs highlight" style="left:287px;top:377px">Tretlux</div>
    <svg class="icon" style="left:266px;top:406px;height:19px" viewBox="0 0 16 19"><path d="M5 1h6l-2 4H7z" fill="var(--yellow)"/><path d="M6 5h4c4 3 5 7 4 10-1 3-11 3-12 0-1-3 0-7 4-10z" fill="var(--yellow)"/></svg>
    <div class="abs highlight" style="left:287px;top:405px">Gehalt bis zu<br>4.500 EUR</div>

    <svg class="icon" style="left:388px;top:473px;width:15px;height:19px" viewBox="0 0 13 16"><path d="M6.5 16S1 10 1 6.2a5.5 5.5 0 0 1 11 0C12 10 6.5 16 6.5 16z" fill="var(--pin)"/><circle cx="6.5" cy="6.2" r="2.3" fill="var(--paper)"/></svg>
    <div class="abs location" style="left:403px;top:473px;font-size:14.5px">Ort: Hannover</div>
  </section>

</main>
</body>
</html>
```